Family Brewery needs a label design for the four different types of beer.

We need a label design for two beer bottle sizes (500 and 700 ml. )
The label design should include the family monogram and company logo, as it would be a corporate gift for the new year from our CEO to business partners and clients. We have one request for showing the company logo on bottle. As it would be the new year edition, we would like to see design "adaptive" in case we would like to keep it after the holidays on an ongoing basis. Our main company direction is design and manufacture of cooling equipment for ice rinks, so it would be fine but not necessary to see design related to our business (if you would like to check the company, there is our website - www.kelvana.ru)
Labels on bottles should be in the same style but vary depending on the variety and taste of beer.
Types of bear
-Pilzner ( 4.4 % of alcohol)
-Honig Pilsner(5.2 % of alcohol)
-Wiener Ale ( 4.7 % of alcohol)
-Weissbier (5.6 % of alcohol)
If you have any questions just message me and i will answer as soon as possible.
Files attached contain the family monogram, company logo ( kelvana ), picture of beer bottles that would be in usage.

```html
<!DOCTYPE html>
<html lang="en">
<head>
<meta charset="utf-8">
<title>Pilzner Label — Family Brewery</title>
<link rel="stylesheet" href="https://fonts.googleapis.com/css2?family=Bebas+Neue&family=Oswald:wght@600&family=Roboto+Condensed:wght@400;700&display=swap">
<style>
  :root {
    --bg: #e9ebea;
    --label: #12141d;
    --gold: #a98e5b;
    --gold-soft: #8c7649;
    --white: #ffffff;
  }
  html, body { margin: 0; padding: 0; overflow: hidden; background: var(--bg); }
  .canvas { width: 1200px; height: 1200px; display: block; }
  .arc-title { font-family: "Oswald", sans-serif; font-weight: 600; font-size: 48px; letter-spacing: 4px; fill: var(--gold); }
  .beer-name { font-family: "Bebas Neue", sans-serif; font-size: 172px; fill: var(--white); letter-spacing: 4px; }
  .spec { font-family: "Roboto Condensed", sans-serif; font-size: 21px; fill: var(--gold); }
  .spec-small { font-size: 13px; }
  .maker { font-family: "Roboto Condensed", sans-serif; font-weight: 700; font-size: 44px; fill: var(--gold); }
  .brand-name { font-family: "Roboto Condensed", sans-serif; font-weight: 700; font-size: 28px; fill: var(--gold); letter-spacing: 2px; }
  .rule { stroke: var(--gold); stroke-width: 2.5; fill: none; }
  .rule-thin { stroke: var(--gold); stroke-width: 1.6; fill: none; }
</style>
</head>
<body>
<svg class="canvas" viewBox="0 0 1000 1000" xmlns="http://www.w3.org/2000/svg">
  <defs>
    <path id="top-arc" d="M200 540 A300 300 0 0 1 800 540"/>
    <path id="bottom-arc" d="M163 460 A337 337 0 0 0 837 460"/>
  </defs>

  <rect width="1000" height="1000" fill="var(--bg)"/>

  <path class="label-shape" fill="var(--label)" d="M178 325 A402 402 0 0 1 822 325 V675 A402 402 0 0 1 178 675 Z"/>

  <g class="rings">
    <path class="rule" d="M196 318 A400 400 0 0 1 804 318"/>
    <path class="rule-thin" d="M214 318 A387 387 0 0 1 786 318"/>
    <path class="rule" d="M196 666 A400 400 0 0 0 804 666"/>
    <path class="rule-thin" d="M214 666 A387 387 0 0 0 786 666"/>
  </g>

  <text class="arc-title"><textPath href="#top-arc" startOffset="50%" text-anchor="middle">FAMILY BREWERY</textPath></text>

  <g class="top-band">
    <path class="rule" d="M230 330 H770 M230 394 H770"/>
    <path class="rule-thin" d="M205 318 H255 V330 M795 318 H745 V330 M205 318 V404 H255 V394 M795 318 V404 H745 V394"/>
    <path class="rule-thin" d="M218 334 V388 M782 334 V388"/>
    <rect x="268" y="344" width="165" height="34" rx="17" fill="var(--gold-soft)" role="img" aria-label="Floral scroll ornament"/>
    <rect x="567" y="344" width="165" height="34" rx="17" fill="var(--gold-soft)" role="img" aria-label="Floral scroll ornament"/>
    <ellipse cx="500" cy="362" rx="62" ry="52" fill="var(--label)" class="rule"/>
    <ellipse cx="500" cy="362" rx="46" ry="40" fill="var(--gold-soft)" role="img" aria-label="Family monogram"/>
    <rect x="472" y="268" width="56" height="32" rx="4" fill="var(--gold-soft)" role="img" aria-label="Crown above monogram"/>
  </g>

  <text class="beer-name" x="500" y="560" text-anchor="middle" textLength="460" lengthAdjust="spacingAndGlyphs">PILZNER</text>

  <g class="bottom-band">
    <path class="rule" d="M230 590 H770 M230 652 H770"/>
    <path class="rule-thin" d="M205 578 H255 V590 M795 578 H745 V590 M205 578 V664 H255 V652 M795 578 H795 M205 664 H255 M795 578 V664 H745 V652"/>
    <path class="rule-thin" d="M218 594 V648 M782 594 V648"/>
    <text class="spec" x="342" y="628" text-anchor="middle">500 ml</text>
    <text class="spec" x="583" y="628">4.4 % <tspan class="spec-small">of alcohol</tspan></text>
    <text class="brand-name" x="500" y="631" text-anchor="middle">KELVANA</text>
  </g>

  <text class="maker"><textPath href="#bottom-arc" startOffset="50%" text-anchor="middle">Кельвана | Kelvana</textPath></text>
</svg>
</body>
</html>
```